Stationery Design Project - Meridan-Vale

Business Cards
Size: 90mm x 55mm

Letterhead
Size: A4 - 210mm x 297mm

With Compliments Slip
Size: DL - 210mm x 99mm

Notepad
Size: 250mm x 140mm

Presentation Folder
Size: A4

Meridan-Vale
*Perth *Brisbane *Seoul *Hongkong

website: www.meridanvale.com.au (Currently live, but being replaced with new one)

Engineering and Technical recruitment company for the Mining, Oil & Gas, Construction & Engineering Sectors
Updates

Industry/Entity Type

Business

```html
<!DOCTYPE html>
<html lang="en">
<head>
<meta charset="utf-8">
<title>Meridan-Vale Stationery</title>
<link href="https://fonts.googleapis.com/css2?family=Maven+Pro:wght@400;500&display=swap" rel="stylesheet">
<style>
  :root {
    --backdrop: #dcdcdc;
    --paper: #f1f1f1;
    --ink: #3c3f44;
    --ink-soft: #6a6e74;
    --brand-blue: #2a68c4;
    --deep-blue: #1d4f8e;
    --shadow: rgba(0, 0, 0, 0.25);
  }
  * { box-sizing: border-box; margin: 0; padding: 0; }
  html, body {
    width: 1200px; height: 900px; overflow: hidden;
    background: var(--backdrop);
    font-family: "Maven Pro", "Helvetica Neue", Arial, sans-serif;
    color: var(--ink);
  }
  .canvas { position: relative; width: 1200px; height: 900px; }
  .sheet {
    position: absolute; background: var(--paper);
    box-shadow: 0 3px 10px var(--shadow);
    overflow: hidden;
  }
  .brand {
    position: absolute; display: flex; align-items: center; gap: 10px;
    font-weight: 400; color: var(--ink); letter-spacing: 0.5px;
  }
  .brand-dot {
    border-radius: 50%; background: var(--brand-blue); flex: none;
  }
  .details { position: absolute; line-height: 1.35; color: var(--ink); }
  .details .label { color: var(--brand-blue); }
  .contact-gap { margin-top: 11px; }

  /* letterhead */
  .letterhead { left: 46px; top: 38px; width: 592px; height: 841px; }
  .letterhead .brand { left: 36px; top: 52px; font-size: 26px; }
  .letterhead .brand-dot { width: 36px; height: 36px; }
  .letterhead .details { left: 34px; top: 725px; font-size: 11.5px; }

  /* business cards */
  .card { width: 321px; height: 192px; border-radius: 14px; }
  .card-front { left: 483px; top: 113px; }
  .card-front .brand { left: 20px; top: 16px; font-size: 16px; gap: 7px; }
  .card-front .brand-dot { width: 22px; height: 22px; }
  .card-name { position: absolute; left: 20px; top: 68px; font-size: 14px; color: var(--brand-blue); font-weight: 400; }
  .card-role { position: absolute; left: 20px; top: 86px; font-size: 7.5px; color: var(--ink-soft); }
  .card-front .details { left: 20px; top: 110px; font-size: 7.5px; color: var(--ink-soft); }
  .card-front .contact-gap { margin-top: 8px; }

  .card-back {
    left: 827px; top: 110px;
    background: linear-gradient(90deg, #f6f7f9 0%, #c9d6e6 22%, #5f86b9 55%, var(--deep-blue) 100%);
  }
  .card-back .brand { left: 102px; top: 84px; font-size: 19px; color: #eef2f7; }
  .card-back .cities { position: absolute; left: 102px; top: 122px; font-size: 11px; color: #ffffff; }
  .card-back .web { position: absolute; left: 116px; top: 170px; font-size: 9px; color: #c9d7ea; }

  /* compliments slip */
  .slip { left: 483px; top: 353px; width: 596px; height: 281px; }
  .slip .brand { left: 24px; top: 42px; font-size: 20px; gap: 8px; }
  .slip .brand-dot { width: 28px; height: 28px; }
  .slip-title { position: absolute; right: 44px; top: 46px; font-size: 20px; color: var(--brand-blue); font-weight: 400; }
  .slip .details { left: 22px; top: 185px; font-size: 11px; }
  .slip .contact-gap { margin-top: 13px; }
</style>
</head>
<body>
<main class="canvas">

  <section class="sheet letterhead" aria-label="Letterhead">
    <div class="brand"><span class="brand-dot"></span>Meridan-Vale</div>
    <address class="details" style="font-style:normal">
      Suite 12, 215 Harlow Street<br>Westbrook<br>Western Australia 6010
      <div class="contact-gap">
        <span class="label">P</span> | 08 6400 2100<br>
        <span class="label">F</span> | 08 6400 2199<br>
        <span class="label">E</span> | info@meridanvale.com.au
      </div>
    </address>
  </section>

  <section class="sheet card card-front" aria-label="Business card front">
    <div class="brand"><span class="brand-dot"></span>Meridan-Vale</div>
    <h2 class="card-name">Liam Carver</h2>
    <p class="card-role">General Manager</p>
    <address class="details" style="font-style:normal">
      Suite 12, 215 Harlow Street<br>Westbrook Western Australia 6010
      <div class="contact-gap">
        <span class="label">P</span> | 08 6400 2100<br>
        <span class="label">F</span> | 08 6400 2199<br>
        <span class="label">E</span> | info@meridanvale.com.au
      </div>
    </address>
  </section>

  <section class="sheet card card-back" aria-label="Business card back">
    <div class="brand">Meridan-Vale</div>
    <p class="cities">·Perth ·Brisbane ·Seoul ·Hongkong</p>
    <p class="web">www.meridanvale.com.au</p>
  </section>

  <section class="sheet slip" aria-label="With compliments slip">
    <div class="brand"><span class="brand-dot"></span>Meridan-Vale</div>
    <h2 class="slip-title">With Compliments</h2>
    <address class="details" style="font-style:normal">
      Suite 12, 215 Harlow Street<br>Westbrook Western Australia 6010
      <div class="contact-gap">
        <span class="label">P</span> | 08 6400 2100<br>
        <span class="label">F</span> | 08 6400 2199<br>
        <span class="label">E</span> | info@meridanvale.com.au
      </div>
    </address>
  </section>

</main>
</body>
</html>
```